Easy Marinade Labels for Butchery Store

Need a set of labels designed for a Butchery Shop. They will sit in the top left corner of the packets as a triangle (7cm each side). Easy because the only major requirement is the label name and some small text saying "Please ask in store to see spec sheet for ingredients". Extra points for finding a fun way to incorporate the logo and/or images of food (garlic bulbs, chilli, spices ect) to enhance the label. List of Marinade Names below: GarlicPepper Mint & RosemarySatayBBQChilli Plum & GingerSundried Tomato & BasilBuffaloHoney SoyHoi-SinPer PeriSpicy CajunTeriyakiBlack Bean Ive also attached the logo and an example of how the label might sit on a packet of meat. Thanks

Target Market(s)

Butchery Deli Shop Customers

Industry/Entity Type

Food Store

Font styles to use
Serif
Sans Serif
Decorative
Other font styles liked:
• Fun font that isn't a generic Quillbrenn Font?

Colors

Designer to choose colors to be used in the design.

Requirements
Must have
• Product Name
• Small text saying "Please ask in store to see spec sheet for ingredients"
Nice to have
• Photos of ingredients that would match that type of marinade - Chilli, Garlic, Spices.
• Tavo Crest Logo - not essential if it doesn't look good on the label / doesn't fit.

```html
<!DOCTYPE html>
<html lang="en">
<head>
<meta charset="utf-8">
<title>Tavo Crest Marinade Labels</title>
<link rel="stylesheet" href="https://fonts.googleapis.com/css2?family=Russo+One&family=Oswald:wght@300;400&display=swap">
<style>
  :root {
    --canvas-bg: #f4f5f6;
    --canvas-edge: #c9ced3;
    --frame-gold: #8c6f3e;
    --label-cream: #f7f4ee;
    --inner-line: #ffffff;
    --title-brown: #9a6a1c;
    --brand-red: #a3161c;
    --fine-print: #4a3b2a;
    --eyebrow: #8a6a2e;
  }
  * { box-sizing: border-box; margin: 0; padding: 0; }
  html, body { width: 1200px; height: 923px; overflow: hidden; }
  body {
    background: radial-gradient(ellipse at center, #ffffff 0%, var(--canvas-bg) 55%, var(--canvas-edge) 100%);
    font-family: "Oswald", sans-serif;
  }
  .label-sheet {
    display: grid;
    grid-template-columns: repeat(3, 298px);
    grid-auto-rows: 148px;
    column-gap: 46px;
    row-gap: 33px;
    padding: 25px 0 0 107px;
  }
  .label {
    position: relative;
    width: 298px;
    height: 148px;
  }
  .label-shape { position: absolute; inset: 0; width: 298px; height: 148px; }
  .layer-frame { fill: var(--frame-gold); }
  .layer-accent { fill: var(--accent); }
  .layer-line { fill: var(--inner-line); }
  .layer-cream { fill: var(--label-cream); }
  .ingredient-art {
    position: absolute;
    left: 131px;
    top: 31px;
    width: 36px;
    height: 21px;
    border-radius: 5px;
    background: var(--art);
  }
  .brand {
    position: absolute;
    left: 0; right: 0;
    top: 54px;
    text-align: center;
    font-family: "Russo One", sans-serif;
    font-size: 15px;
    line-height: 18px;
    color: var(--brand-red);
  }
  .eyebrow {
    position: absolute;
    left: 0; right: 0;
    top: 85px;
    text-align: center;
    font-size: 6.5px;
    line-height: 8px;
    letter-spacing: 2px;
    color: var(--eyebrow);
    text-transform: uppercase;
  }
  .flavour {
    position: absolute;
    left: 0; right: 0;
    top: 96px;
    text-align: center;
    font-family: "Russo One", sans-serif;
    font-weight: 400;
    font-size: 21px;
    line-height: 1;
    color: var(--title-brown);
    white-space: nowrap;
  }
  .flavour.two-line { top: 93px; font-size: 17px; line-height: 0.95; }
  .label:first-child .eyebrow { top: 82px; }
  .fine-print {
    position: absolute;
    left: 0; right: 0;
    top: 128px;
    text-align: center;
    font-size: 9px;
    line-height: 11px;
    font-weight: 300;
    color: var(--fine-print);
    white-space: nowrap;
  }
  .hidden-defs { position: absolute; width: 0; height: 0; }
</style>
</head>
<body>
<svg class="hidden-defs" aria-hidden="true">
  <defs>
    <polygon id="tri" points="149,0 298,148 0,148"/>
  </defs>
</svg>

<main class="label-sheet">

  <article class="label" style="--accent:#2f8a3c; --art:radial-gradient(circle at 50% 45%, #d2301f 0 40%, #3f8f3a 80%)">
    <svg class="label-shape" viewBox="0 0 298 148" aria-hidden="true">
      <use href="#tri" class="layer-frame"/>
      <use href="#tri" class="layer-accent" transform="translate(149 86.6) scale(0.955) translate(-149 -86.6)"/>
      <use href="#tri" class="layer-line" transform="translate(149 86.6) scale(0.93) translate(-149 -86.6)"/>
      <use href="#tri" class="layer-cream" transform="translate(149 86.6) scale(0.915) translate(-149 -86.6)"/>
    </svg>
    <div class="ingredient-art" role="img" aria-label="Tomato with basil leaves"></div>
    <p class="brand">Tavo Crest</p>
    <p class="eyebrow">Marinated with</p>
    <h2 class="flavour two-line">Sundried Tomato<br>&amp; Basil</h2>
    <p class="fine-print">Please ask in store to see spec sheet for ingredients</p>
  </article>

  <article class="label" style="--accent:#b9a89a; --art:radial-gradient(circle, #f3ede2 0 45%, #d8ccb8 85%)">
    <svg class="label-shape" viewBox="0 0 298 148" aria-hidden="true">
      <use href="#tri" class="layer-frame"/>
      <use href="#tri" class="layer-accent" transform="translate(149 86.6) scale(0.955) translate(-149 -86.6)"/>
      <use href="#tri" class="layer-line" transform="translate(149 86.6) scale(0.93) translate(-149 -86.6)"/>
      <use href="#tri" class="layer-cream" transform="translate(149 86.6) scale(0.915) translate(-149 -86.6)"/>
    </svg>
    <div class="ingredient-art" role="img" aria-label="Garlic bulbs"></div>
    <p class="brand">Tavo Crest</p>
    <p class="eyebrow">Marinated with</p>
    <h2 class="flavour">Garlic Sprinkle</h2>
    <p class="fine-print">Please ask in store to see spec sheet for ingredients</p>
  </article>

  <article class="label" style="--accent:#6b4a2e; --art:radial-gradient(circle, #6a4a32 0 45%, #c9c2b6 90%)">
    <svg class="label-shape" viewBox="0 0 298 148" aria-hidden="true">
      <use href="#tri" class="layer-frame"/>
      <use href="#tri" class="layer-accent" transform="translate(149 86.6) scale(0.955) translate(-149 -86.6)"/>
      <use href="#tri" class="layer-line" transform="translate(149 86.6) scale(0.93) translate(-149 -86.6)"/>
      <use href="#tri" class="layer-cream" transform="translate(149 86.6) scale(0.915) translate(-149 -86.6)"/>
    </svg>
    <div class="ingredient-art" role="img" aria-label="Buffalo head with horns"></div>
    <p class="brand">Tavo Crest</p>
    <p class="eyebrow">Marinated with</p>
    <h2 class="flavour">Buffalo Spices</h2>
    <p class="fine-print">Please ask in store to see spec sheet for ingredients</p>
  </article>

  <article class="label" style="--accent:#d9301c; --art:linear-gradient(135deg, #d62a1a 30%, #ece4d4 90%)">
    <svg class="label-shape" viewBox="0 0 298 148" aria-hidden="true">
      <use href="#tri" class="layer-frame"/>
      <use href="#tri" class="layer-accent" transform="translate(149 86.6) scale(0.955) translate(-149 -86.6)"/>
      <use href="#tri" class="layer-line" transform="translate(149 86.6) scale(0.93) translate(-149 -86.6)"/>
      <use href="#tri" class="layer-cream" transform="translate(149 86.6) scale(0.915) translate(-149 -86.6)"/>
    </svg>
    <div class="ingredient-art" role="img" aria-label="Red chilli with garlic"></div>
    <p class="brand">Tavo Crest</p>
    <p class="eyebrow">Marinated with</p>
    <h2 class="flavour">Peri Peri</h2>
    <p class="fine-print">Please ask in store to see spec sheet for ingredients</p>
  </article>

  <article class="label" style="--accent:#6a3ca0; --art:linear-gradient(90deg, #b07a3e 20%, #5b2a8c 80%)">
    <svg class="label-shape" viewBox="0 0 298 148" aria-hidden="true">
      <use href="#tri" class="layer-frame"/>
      <use href="#tri" class="layer-accent" transform="translate(149 86.6) scale(0.955) translate(-149 -86.6)"/>
      <use href="#tri" class="layer-line" transform="translate(149 86.6) scale(0.93) translate(-149 -86.6)"/>
      <use href="#tri" class="layer-cream" transform="translate(149 86.6) scale(0.915) translate(-149 -86.6)"/>
    </svg>
    <div class="ingredient-art" role="img" aria-label="Plums with ginger root"></div>
    <p class="brand">Tavo Crest</p>
    <p class="eyebrow">Marinated with</p>
    <h2 class="flavour">Plum &amp; Ginger</h2>
    <p class="fine-print">Please ask in store to see spec sheet for ingredients</p>
  </article>

  <article class="label" style="--accent:#333333; --art:linear-gradient(180deg, #444 30%, #a08a60 100%)">
    <svg class="label-shape" viewBox="0 0 298 148" aria-hidden="true">
      <use href="#tri" class="layer-frame"/>
      <use href="#tri" class="layer-accent" transform="translate(149 86.6) scale(0.955) translate(-149 -86.6)"/>
      <use href="#tri" class="layer-line" transform="translate(149 86.6) scale(0.93) translate(-149 -86.6)"/>
      <use href="#tri" class="layer-cream" transform="translate(149 86.6) scale(0.915) translate(-149 -86.6)"/>
    </svg>
    <div class="ingredient-art" role="img" aria-label="Kettle barbecue grill"></div>
    <p class="brand">Tavo Crest</p>
    <p class="eyebrow">Marinated with</p>
    <h2 class="flavour">BBQ Sauce</h2>
    <p class="fine-print">Please ask in store to see spec sheet for ingredients</p>
  </article>

  <article class="label" style="--accent:#555555; --art:radial-gradient(circle, #2a2a2a 0 55%, #6a6a6a 95%)">
    <svg class="label-shape" viewBox="0 0 298 148" aria-hidden="true">
      <use href="#tri" class="layer-frame"/>
      <use href="#tri" class="layer-accent" transform="translate(149 86.6) scale(0.955) translate(-149 -86.6)"/>
      <use href="#tri" class="layer-line" transform="translate(149 86.6) scale(0.93) translate(-149 -86.6)"/>
      <use href="#tri" class="layer-cream" transform="translate(149 86.6) scale(0.915) translate(-149 -86.6)"/>
    </svg>
    <div class="ingredient-art" role="img" aria-label="Pile of black peppercorns"></div>
    <p class="brand">Tavo Crest</p>
    <p class="eyebrow">Marinated with</p>
    <h2 class="flavour">Pepper Sprinkle</h2>
    <p class="fine-print">Please ask in store to see spec sheet for ingredients</p>
  </article>

  <article class="label" style="--accent:#d4b21a; --art:radial-gradient(circle, #ffd43a 0 50%, #e8b21c 95%)">
    <svg class="label-shape" viewBox="0 0 298 148" aria-hidden="true">
      <use href="#tri" class="layer-frame"/>
      <use href="#tri" class="layer-accent" transform="translate(149 86.6) scale(0.955) translate(-149 -86.6)"/>
      <use href="#tri" class="layer-line" transform="translate(149 86.6) scale(0.93) translate(-149 -86.6)"/>
      <use href="#tri" class="layer-cream" transform="translate(149 86.6) scale(0.915) translate(-149 -86.6)"/>
    </svg>
    <div class="ingredient-art" role="img" aria-label="Honeycomb"></div>
    <p class="brand">Tavo Crest</p>
    <p class="eyebrow">Marinated with</p>
    <h2 class="flavour">Honey Soy</h2>
    <p class="fine-print">Please ask in store to see spec sheet for ingredients</p>
  </article>

  <article class="label" style="--accent:#1a237e; --art:linear-gradient(135deg, #e6e6ee 10%, #3a4496 90%)">
    <svg class="label-shape" viewBox="0 0 298 148" aria-hidden="true">
      <use href="#tri" class="layer-frame"/>
      <use href="#tri" class="layer-accent" transform="translate(149 86.6) scale(0.955) translate(-149 -86.6)"/>
      <use href="#tri" class="layer-line" transform="translate(149 86.6) scale(0.93) translate(-149 -86.6)"/>
      <use href="#tri" class="layer-cream" transform="translate(149 86.6) scale(0.915) translate(-149 -86.6)"/>
    </svg>
    <div class="ingredient-art" role="img" aria-label="Regional Cajun flag"></div>
    <p class="brand">Tavo Crest</p>
    <p class="eyebrow">Marinated with</p>
    <h2 class="flavour">Spicy Cajun</h2>
    <p class="fine-print">Please ask in store to see spec sheet for ingredients</p>
  </article>

  <article class="label" style="--accent:#2f7d4f; --art:radial-gradient(circle, #1e1e1e 0 55%, #4a4a4a 95%)">
    <svg class="label-shape" viewBox="0 0 298 148" aria-hidden="true">
      <use href="#tri" class="layer-frame"/>
      <use href="#tri" class="layer-accent" transform="translate(149 86.6) scale(0.955) translate(-149 -86.6)"/>
      <use href="#tri" class="layer-line" transform="translate(149 86.6) scale(0.93) translate(-149 -86.6)"/>
      <use href="#tri" class="layer-cream" transform="translate(149 86.6) scale(0.915) translate(-149 -86.6)"/>
    </svg>
    <div class="ingredient-art" role="img" aria-label="Black beans"></div>
    <p class="brand">Tavo Crest</p>
    <p class="eyebrow">Marinated with</p>
    <h2 class="flavour">Black Bean Sauce</h2>
    <p class="fine-print">Please ask in store to see spec sheet for ingredients</p>
  </article>

  <article class="label" style="--accent:#b51d1d; --art:linear-gradient(120deg, #d4261a 40%, #3c8a2e 100%)">
    <svg class="label-shape" viewBox="0 0 298 148" aria-hidden="true">
      <use href="#tri" class="layer-frame"/>
      <use href="#tri" class="layer-accent" transform="translate(149 86.6) scale(0.955) translate(-149 -86.6)"/>
      <use href="#tri" class="layer-line" transform="translate(149 86.6) scale(0.93) translate(-149 -86.6)"/>
      <use href="#tri" class="layer-cream" transform="translate(149 86.6) scale(0.915) translate(-149 -86.6)"/>
    </svg>
    <div class="ingredient-art" role="img" aria-label="Red chillies"></div>
    <p class="brand">Tavo Crest</p>
    <p class="eyebrow">Marinated with</p>
    <h2 class="flavour">Chilli</h2>
    <p class="fine-print">Please ask in store to see spec sheet for ingredients</p>
  </article>

  <article class="label" style="--accent:#e0531a; --art:#d8321c">
    <svg class="label-shape" viewBox="0 0 298 148" aria-hidden="true">
      <use href="#tri" class="layer-frame"/>
      <use href="#tri" class="layer-accent" transform="translate(149 86.6) scale(0.955) translate(-149 -86.6)"/>
      <use href="#tri" class="layer-line" transform="translate(149 86.6) scale(0.93) translate(-149 -86.6)"/>
      <use href="#tri" class="layer-cream" transform="translate(149 86.6) scale(0.915) translate(-149 -86.6)"/>
    </svg>
    <div class="ingredient-art" role="img" aria-label="Chinese flag"></div>
    <p class="brand">Tavo Crest</p>
    <p class="eyebrow">Marinated with</p>
    <h2 class="flavour">Hoi-Sin Sauce</h2>
    <p class="fine-print">Please ask in store to see spec sheet for ingredients</p>
  </article>

  <article class="label" style="--accent:#6fb8a3; --art:linear-gradient(135deg, #4f9a4a 20%, #8aa78a 100%)">
    <svg class="label-shape" viewBox="0 0 298 148" aria-hidden="true">
      <use href="#tri" class="layer-frame"/>
      <use href="#tri" class="layer-accent" transform="translate(149 86.6) scale(0.955) translate(-149 -86.6)"/>
      <use href="#tri" class="layer-line" transform="translate(149 86.6) scale(0.93) translate(-149 -86.6)"/>
      <use href="#tri" class="layer-cream" transform="translate(149 86.6) scale(0.915) translate(-149 -86.6)"/>
    </svg>
    <div class="ingredient-art" role="img" aria-label="Mint leaves and rosemary sprigs"></div>
    <p class="brand">Tavo Crest</p>
    <p class="eyebrow">Marinated with</p>
    <h2 class="flavour">Mint &amp; Rosemary</h2>
    <p class="fine-print">Please ask in store to see spec sheet for ingredients</p>
  </article>

  <article class="label" style="--accent:#7a3b2e; --art:linear-gradient(90deg, #8a5a2a, #c08a4a)">
    <svg class="label-shape" viewBox="0 0 298 148" aria-hidden="true">
      <use href="#tri" class="layer-frame"/>
      <use href="#tri" class="layer-accent" transform="translate(149 86.6) scale(0.955) translate(-149 -86.6)"/>
      <use href="#tri" class="layer-line" transform="translate(149 86.6) scale(0.93) translate(-149 -86.6)"/>
      <use href="#tri" class="layer-cream" transform="translate(149 86.6) scale(0.915) translate(-149 -86.6)"/>
    </svg>
    <div class="ingredient-art" role="img" aria-label="Satay skewers"></div>
    <p class="brand">Tavo Crest</p>
    <p class="eyebrow">Marinated with</p>
    <h2 class="flavour">Satay</h2>
    <p class="fine-print">Please ask in store to see spec sheet for ingredients</p>
  </article>

  <article class="label" style="--accent:#c2182b; --art:linear-gradient(180deg, #f3efef 0%, #e4c6c9 100%)">
    <svg class="label-shape" viewBox="0 0 298 148" aria-hidden="true">
      <use href="#tri" class="layer-frame"/>
      <use href="#tri" class="layer-accent" transform="translate(149 86.6) scale(0.955) translate(-149 -86.6)"/>
      <use href="#tri" class="layer-line" transform="translate(149 86.6) scale(0.93) translate(-149 -86.6)"/>
      <use href="#tri" class="layer-cream" transform="translate(149 86.6) scale(0.915) translate(-149 -86.6)"/>
    </svg>
    <div class="ingredient-art" role="img" aria-label="Japanese flag"></div>
    <p class="brand">Tavo Crest</p>
    <p class="eyebrow">Marinated with</p>
    <h2 class="flavour">Teriyaki Sauce</h2>
    <p class="fine-print">Please ask in store to see spec sheet for ingredients</p>
  </article>

</main>
</body>
</html>
```